LABEL DESIGN for our Hemp oil extract headache relief roll on

We need a pure, elegant and natural label design for our new product from Velmora CBD. We make natural and hand made products with CBD oil & other essential oils to improve wellness being. We would like to see natural, earthy and nice labels.

Target Market(s)

Gender: Feminine

Font styles to use
Serif
Sans Serif
Script

Colors
eea4c8
ffffff
b7a5cd
cadf82
7f7f7f

Requirements
Must have
• Measures of the label should be 2.35 x 2 inches.
Nice to have
• Herb leafs
Should not have
• Marijuana leafs

```html
<!DOCTYPE html>
<html lang="en">
<head>
<meta charset="utf-8">
<title>Soft Calm Roll-On Label – Velmora CBD</title>
<link rel="stylesheet" href="https://fonts.googleapis.com/css2?family=Raleway:wght@300;700&family=Fira+Sans+Extra+Condensed:wght@300;400&display=swap">
<style>
  :root {
    --backdrop: #8a8a8a;
    --paper: #ffffff;
    --teal: #03a89d;
    --ink: #6c6d75;
    --ink-soft: #7a7a7a;
    --rule: #ececec;
    --botanical-a: #f1f1f1;
    --botanical-b: #ffffff;
  }
  * { margin: 0; padding: 0; box-sizing: border-box; }
  html, body {
    width: 1200px; height: 1023px; overflow: hidden;
    background: var(--backdrop);
  }
  .label {
    position: absolute; left: 70px; top: 52px;
    width: 1075px; height: 915px;
    background: var(--paper);
  }
  .front-panel {
    position: absolute; left: 0; top: 0; width: 537px; height: 915px;
    border-right: 1px solid var(--rule);
  }
  .botanical-wreath {
    position: absolute; left: 10px; top: 20px; width: 520px; height: 520px;
    border-radius: 50%;
    background: radial-gradient(circle, var(--botanical-a) 0%, var(--botanical-a) 55%, var(--botanical-b) 72%);
  }
  .brand-disc {
    position: absolute; left: 106px; top: 184px; width: 324px; height: 324px;
    border-radius: 50%; background: var(--teal);
    display: flex; align-items: center; justify-content: center;
  }
  .brand-name {
    font-family: "Raleway", sans-serif; font-weight: 700;
    font-size: 66px; line-height: 1.05; text-align: center;
    color: var(--paper);
  }
  .product-type {
    position: absolute; left: 0; width: 537px; text-align: center;
    font-family: "Raleway", sans-serif; color: var(--ink);
  }
  .product-type--extract { top: 535px; font-size: 36px; font-weight: 300; }
  .product-type--format { top: 588px; font-size: 36px; font-weight: 700; }
  .benefit-band {
    position: absolute; left: 0; top: 657px; width: 537px; height: 77px;
    background: var(--teal); color: var(--paper);
    font-family: "Raleway", sans-serif; font-weight: 700; font-size: 47px;
    display: flex; align-items: center; justify-content: center;
  }
  .tagline {
    position: absolute; left: 0; top: 742px; width: 537px; text-align: center;
    font-family: "Raleway", sans-serif; font-weight: 700; font-size: 46px;
    color: var(--ink);
  }
  .info-panel {
    position: absolute; left: 582px; top: 57px; width: 470px;
    font-family: "Fira Sans Extra Condensed", sans-serif; font-weight: 300;
    font-size: 30px; line-height: 46px; color: var(--ink-soft);
  }
  .info-block { margin-bottom: 44px; }
  .info-heading { font-weight: 400; color: var(--ink); }
</style>
</head>
<body>
  <main class="label">
    <section class="front-panel">
      <div class="botanical-wreath" role="img" aria-label="Faint line drawing of herbs, flowers and seeds in a wreath"></div>
      <div class="brand-disc">
        <p class="brand-name">Soft<br>Calm</p>
      </div>
      <p class="product-type product-type--extract">Hemp Oil Extract</p>
      <p class="product-type product-type--format">Roll-On</p>
      <div class="benefit-band">Headache Releaf</div>
      <p class="tagline">Fast &amp; Natural</p>
    </section>
    <section class="info-panel">
      <p class="info-block">Natural and therapeutic balm,<br>made with the finest and puresr Hemp<br>from Colorado, know for its healing &amp;<br>restorative properties.</p>
      <p class="info-block"><span class="info-heading">Direction:</span> Massage into skin.<br>Repeat as needed.</p>
      <p class="info-block"><span class="info-heading">Ingredients:</span> CBD Oil 200mg<br>rosmery, mint, beeswax, lavanda</p>
      <p class="info-block"><span class="info-heading">Hecho Por Velmora CBD</span><br>BOULDER, Colorado, USA<br>www,velmoracbd.com</p>
    </section>
  </main>
</body>
</html>
```